Pelican Shoals Postcard Design

I am a real estate agent
I am marketing a gulf access waterfront community is southwest florida. I would like to do Just Listed and Just Sold post cards

So this will be two different post cards

In addition to the pictures I have uploaded mock ups of an idea of what I would like for the front and the back

I would like this done glossy on both sides

```html
<!DOCTYPE html>
<html lang="en">
<head>
<meta charset="utf-8">
<title>Pelican Shoals Just Sold Postcard – Back</title>
<link rel="stylesheet" href="https://fonts.googleapis.com/css2?family=PT+Sans:wght@400;700&display=swap">
<style>
  :root {
    --orange-deep: #f15a0a;
    --orange-soft: #f47b3e;
    --white: #ffffff;
    --ink: #111111;
    --rule: #ffffff;
  }
  * { box-sizing: border-box; margin: 0; padding: 0; }
  html, body { width: 1200px; height: 927px; overflow: hidden; background: var(--white); }
  body { font-family: "PT Sans", Arial, sans-serif; }

  .postcard { position: relative; width: 1200px; height: 927px; background: var(--white); }

  .message-panel { position: absolute; left: 0; top: 0; width: 585px; height: 927px; color: var(--white); }
  .sale-band { position: absolute; left: 0; top: 0; width: 585px; height: 333px; background: var(--orange-deep); }
  .contact-band { position: absolute; left: 0; top: 333px; width: 585px; height: 494px; background: var(--orange-soft); }
  .footer-stripe { position: absolute; left: 0; top: 827px; width: 585px; height: 44px; background: var(--orange-deep); }
  .footer-base { position: absolute; left: 0; top: 871px; width: 585px; height: 56px; background: var(--orange-soft); }

  .sale-intro { position: absolute; left: 52px; top: 116px; font-size: 31px; line-height: 36px; }
  .sale-line { position: absolute; left: 52px; top: 246px; font-size: 31px; display: flex; align-items: flex-end; gap: 14px; }
  .blank { display: inline-block; border-bottom: 2px solid var(--rule); height: 2px; margin-bottom: 10px; }
  .blank--price { width: 190px; }
  .blank--date { width: 190px; }

  .contact-heading { position: absolute; left: 52px; top: 366px; font-size: 31px; line-height: 40px; }
  .contact-heading strong { font-weight: 700; font-size: 35px; }

  .interest-list { position: absolute; left: 52px; top: 462px; list-style: none; }
  .interest-item { display: flex; align-items: center; height: 74px; margin-bottom: 36px; font-size: 27px; font-weight: 700; }
  .checkbox { width: 80px; height: 74px; margin-right: 30px; flex: none; }

  .call-line { position: absolute; left: 52px; top: 688px; font-size: 35px; font-weight: 700; }
  .call-line .agent-name { font-weight: 400; font-size: 40px; margin-left: 14px; }

  .contact-details { position: absolute; left: 58px; top: 758px; display: flex; align-items: center; font-size: 16px; font-weight: 700; }
  .contact-details svg { flex: none; }
  .phone { display: flex; align-items: center; gap: 12px; margin-right: 46px; }
  .email { display: flex; align-items: center; gap: 12px; }

  .brand { position: absolute; left: 600px; top: 44px; display: flex; align-items: center; gap: 12px; color: var(--ink); }
  .brand-mark { width: 26px; height: 26px; border-radius: 50%; background: var(--ink); }
  .brand-name { font-size: 24px; font-weight: 700; }
  .return-address { position: absolute; left: 600px; top: 128px; font-size: 22px; line-height: 27px; font-weight: 700; color: var(--ink); }

  .postage-box { position: absolute; left: 990px; top: 45px; width: 171px; height: 150px; border: 2px solid var(--ink); padding: 18px 20px; font-size: 27px; line-height: 32px; color: var(--ink); }
</style>
</head>
<body>
<main class="postcard">
  <section class="message-panel">
    <div class="sale-band"></div>
    <div class="contact-band"></div>
    <div class="footer-stripe"></div>
    <div class="footer-base"></div>

    <p class="sale-intro">on your block of Pelican Shoals<br>has just sold at:</p>
    <p class="sale-line">$ <span class="blank blank--price"></span> on <span class="blank blank--date"></span></p>

    <p class="contact-heading"><strong>PLEASE CONTACT ME,</strong> if you<br>are interested in:</p>

    <ul class="interest-list">
      <li class="interest-item">
        <svg class="checkbox" viewBox="0 0 80 74" aria-hidden="true">
          <rect x="2" y="14" width="60" height="58" fill="none" stroke="#111" stroke-width="2"/>
          <path d="M10 40 L22 34 L32 50 Q48 18 76 2 Q52 26 34 66 L30 66 Z" fill="#111"/>
        </svg>
        Buying a property in the area
      </li>
      <li class="interest-item">
        <svg class="checkbox" viewBox="0 0 80 74" aria-hidden="true">
          <rect x="2" y="14" width="60" height="58" fill="none" stroke="#111" stroke-width="2"/>
          <path d="M10 40 L22 34 L32 50 Q48 18 76 2 Q52 26 34 66 L30 66 Z" fill="#111"/>
        </svg>
        Selling a property in the area
      </li>
    </ul>

    <p class="call-line">Call or email: <span class="agent-name">Avery Marsh</span></p>

    <div class="contact-details">
      <span class="phone">
        <svg width="22" height="22" viewBox="0 0 24 24" aria-hidden="true"><path d="M6.6 10.8a15 15 0 0 0 6.6 6.6l2.2-2.2a1 1 0 0 1 1-.25 11.4 11.4 0 0 0 3.6.6 1 1 0 0 1 1 1V20a1 1 0 0 1-1 1A17 17 0 0 1 3 4a1 1 0 0 1 1-1h3.5a1 1 0 0 1 1 1c0 1.25.2 2.45.6 3.6a1 1 0 0 1-.25 1z" fill="#fff"/></svg>
        941-555-0147
      </span>
      <span class="email">
        <svg width="28" height="20" viewBox="0 0 28 20" aria-hidden="true"><rect x="1" y="1" width="26" height="18" fill="none" stroke="#fff" stroke-width="2"/><path d="M1 1 L14 11 L27 1" fill="none" stroke="#fff" stroke-width="2"/></svg>
        averymarsh@example.com
      </span>
    </div>
  </section>

  <header class="brand">
    <span class="brand-mark" aria-hidden="true"></span>
    <span class="brand-name">Harbor Key Realty</span>
  </header>
  <address class="return-address" style="font-style: normal;">PO Box 418<br>Cape Heron, FL 33900</address>

  <div class="postage-box">Place<br>Postage<br>Here</div>
</main>
</body>
</html>
```